Design a product reviews website

We need a website design and simple logo for the brand Pivlo.com. The website will provide reviews of technology products and services. The brand and website should be approachable but should also be trustworthy and high quality. The deliverable should be designs, specs and assets that I can provide to a development team to build the website.

Target Market(s)

People researching products to buy.

Industry/Entity Type

Product

Logo Text

Pivlo.com

Number of Pages Required

5+ page

Font styles to use
Sans Serif

Colors
0492cd
0355a3
3176b5
33a6d7
85cae6
85abd2
cedeed
cee9f5

Requirements
Must have
• - Designs for the Homepage, Category and Article pages.
• - Designs for web and mobile.
• - Designs details for the engineering team to use for development.
• - I'm open to other colors than the preferences I chose but I'm more likely to like blues, greys and blacks.

```html
<!DOCTYPE html>
<html lang="en">
<head>
<meta charset="utf-8">
<title>Pivlo.com — Product And Services Reviews</title>
<link rel="stylesheet" href="https://fonts.googleapis.com/css2?family=Raleway:wght@400;500;600;700&display=swap">
<style>
:root{
  --blue:#33a6d7;
  --blue-deep:#0492cd;
  --ink:#222222;
  --text:#444444;
  --muted:#666666;
  --line:#e3e3e3;
  --soft:#f2f2f2;
  --white:#ffffff;
  --footer:#1d1d1d;
}
*{box-sizing:border-box;margin:0;padding:0}
html,body{width:1200px;height:2403px;overflow:hidden;background:var(--white);font-family:"Raleway",sans-serif;color:var(--text)}
.page{position:relative;width:1200px;height:2403px}

/* hero */
.hero{position:absolute;left:0;top:0;width:1200px;height:650px;overflow:hidden}
.hero-photo{position:absolute;inset:0;background:
  radial-gradient(ellipse at 62% 55%,#6a6d70 0%,#45484b 35%,#26282a 70%,#161718 100%)}
.hero-shade{position:absolute;inset:0;background:rgba(0,0,0,.25)}
.brand{position:absolute;left:99px;top:28px;font-size:28px;font-weight:700;color:var(--white);letter-spacing:.5px}
.brand span{color:var(--blue)}
.menu-btn{position:absolute;left:1064px;top:26px;width:36px;height:36px;border:2px solid var(--white);border-radius:50%}
.menu-btn svg{position:absolute;left:9px;top:10px}
.hero-title{position:absolute;left:0;top:242px;width:1200px;text-align:center;color:var(--white);font-size:35px;font-weight:400;line-height:36px}
.hero-sub{position:absolute;left:0;top:330px;width:1200px;text-align:center;color:#e6e6e6;font-size:13px}
.search{position:absolute;left:429px;top:374px;width:283px;height:32px;border:2px solid #e6e6e6;border-radius:16px;background:rgba(255,255,255,.18);color:#ddd;font-size:12px;line-height:28px;padding-left:20px}
.search-btn{position:absolute;left:727px;top:368px;width:43px;height:43px;border-radius:50%;background:var(--blue);border:3px solid var(--white)}
.search-btn svg{position:absolute;left:11px;top:11px}

/* sidebar */
.categories{position:absolute;left:99px;top:694px;width:231px;border:1px solid var(--line)}
.categories h2{height:41px;background:var(--blue);color:var(--white);font-size:17px;font-weight:600;text-align:center;line-height:41px;letter-spacing:.5px}
.cat-list{list-style:none}
.cat-list li{height:35px;line-height:35px;border-top:1px solid var(--line);padding-left:38px;font-size:12.5px;color:#555;position:relative}
.cat-list li:first-child{border-top:0}
.cat-list li::before{content:"›";position:absolute;left:15px;top:-1px;color:#aaa;font-size:15px}
.cat-list li.active{background:var(--soft)}

/* cards */
.col{position:absolute;display:flex;flex-direction:column}
.col-side{left:99px;top:1014px;width:231px;gap:30px}
.col-a{left:365px;top:755px;width:341px;gap:29px}
.col-b{left:732px;top:756px;width:343px;gap:30px}
.card{border:1px solid var(--line);box-shadow:0 1px 3px rgba(0,0,0,.08);padding:8px 8px 0;background:var(--white)}
.card-media{position:relative;width:100%}
.tags{position:absolute;right:9px;top:9px;display:flex;flex-direction:column;align-items:flex-end;gap:7px}
.tag{width:85px;height:22px;border-radius:11px;font-size:9.5px;font-weight:700;text-align:center;line-height:22px;letter-spacing:.5px}
.tag-home{background:var(--white);color:var(--blue)}
.tag-speakers{background:var(--blue);color:var(--white)}
.card-title{text-align:center;color:var(--ink);font-size:15px;font-weight:600;margin-top:16px}
.meta{display:flex;margin:13px auto 26px;width:234px;height:29px;border:1px solid var(--line)}
.meta .author{display:flex;align-items:center;gap:9px;padding-left:6px;width:124px;border-right:1px solid var(--line);font-size:11.5px;color:#333}
.meta .avatar{width:23px;height:23px;background:#9a8270}
.meta .date{flex:1;text-align:center;line-height:27px;font-size:11.5px;color:#333}
.col-side .meta{width:208px}
.col-side .meta .author{width:112px}

/* tabs */
.tabs{position:absolute;left:365px;top:694px;width:736px;height:35px;border-bottom:2px solid var(--blue);display:flex;align-items:center}
.tab{font-size:12.5px;font-weight:700;color:#333;letter-spacing:.5px;padding:0 22px;border-left:1px solid #ccc;line-height:14px}
.tab.active{background:var(--blue);color:var(--white);height:35px;line-height:35px;border:0;width:186px;text-align:center;padding:0}
.tab.active + .tab{border-left:0}
.tab-arrows{position:absolute;right:0;top:3px;display:flex;gap:8px}
.tab-arrows span{width:20px;height:18px;border:1px solid #999;position:relative}
.tab-arrows svg{position:absolute;left:3px;top:3px}

.load-more{position:absolute;left:535px;top:2281px;width:128px;height:42px;border-radius:21px;background:var(--blue);border:2px solid var(--blue-deep);color:var(--white);font-size:11.5px;font-weight:700;text-align:center;line-height:38px;letter-spacing:.5px}

.footer{position:absolute;left:0;top:2350px;width:1200px;height:53px;background:var(--footer);color:#ddd;font-size:13px;text-align:center;line-height:53px}
.footer b{color:var(--white)}
</style>
</head>
<body>
<div class="page">
  <header class="hero">
    <div class="hero-photo" role="img" aria-label="Dark close-up photo of a silver perforated desktop computer tower beside a keyboard"></div>
    <div class="hero-shade"></div>
    <div class="brand">Pivlo<span>.com</span></div>
    <div class="menu-btn"><svg width="14" height="12" viewBox="0 0 14 12"><path d="M0 1h14M0 6h14M0 11h14" stroke="#fff" stroke-width="2"/></svg></div>
    <h1 class="hero-title">The Best Product And Services Reviews<br>And Rankings</h1>
    <p class="hero-sub">Simply dummy text of the printing and typesetting industry.</p>
    <div class="search">Search</div>
    <div class="search-btn"><svg width="15" height="15" viewBox="0 0 15 15"><circle cx="6" cy="6" r="4.5" fill="none" stroke="#fff" stroke-width="2.2"/><path d="M9.3 9.3L13.5 13.5" stroke="#fff" stroke-width="2.6" stroke-linecap="round"/></svg></div>
  </header>

  <aside class="categories">
    <h2>CATEGORIES</h2>
    <ul class="cat-list">
      <li>APPLIANCES</li>
      <li class="active">COMPUTERS</li>
      <li>ELECTRONIC</li>
      <li>HOME SECURITY</li>
      <li>MOBILE</li>
      <li>SMART HOME</li>
      <li>SOFTWARE</li>
    </ul>
  </aside>

  <div class="col col-side">
    <article class="card">
      <div class="card-media" style="height:231px;background:linear-gradient(180deg,#8a5a4a 0%,#c9b9b0 45%,#e9e6e4 100%)" role="img" aria-label="White home alarm base station with pink buttons on a counter">
        <div class="tags"><span class="tag tag-speakers">SPEAKERS</span></div>
      </div>
      <h3 class="card-title">Lorem Ipsum Dolor</h3>
      <div class="meta"><span class="author"><i class="avatar"></i>Rowan Ellis</span><span class="date">Aug 11, 2016</span></div>
    </article>
    <article class="card">
      <div class="card-media" style="height:378px;background:linear-gradient(180deg,#e8eaea 0%,#d4d2cc 55%,#c9c7c2 100%)" role="img" aria-label="Bright modern white kitchen with bar stools at an island">
        <div class="tags"><span class="tag tag-home">HOME</span><span class="tag tag-speakers">SPEAKERS</span></div>
      </div>
      <h3 class="card-title">Lorem Ipsum Dolor</h3>
      <div class="meta"><span class="author"><i class="avatar"></i>Rowan Ellis</span><span class="date">Aug 11, 2016</span></div>
    </article>
    <article class="card">
      <div class="card-media" style="height:248px;background:linear-gradient(180deg,#2a2a2a 0%,#1a1a1a 100%)" role="img" aria-label="Close-up of a black fabric speaker grille">
        <div class="tags"><span class="tag tag-home">HOME</span></div>
      </div>
      <h3 class="card-title">Lorem Ipsum Dolor</h3>
      <div class="meta"><span class="author"><i class="avatar"></i>Rowan Ellis</span><span class="date">Aug 11, 2016</span></div>
    </article>
  </div>

  <nav class="tabs">
    <span class="tab active">LATEST&nbsp; COMPARISONS</span>
    <span class="tab">PRODUCT ARTICLE</span>
    <span class="tab">POPULAR</span>
    <span class="tab">NEW</span>
    <div class="tab-arrows">
      <span><svg width="12" height="10" viewBox="0 0 12 10"><path d="M11 5H1M5 1L1 5l4 4" fill="none" stroke="#888" stroke-width="1.2"/></svg></span>
      <span><svg width="12" height="10" viewBox="0 0 12 10"><path d="M1 5h10M7 1l4 4-4 4" fill="none" stroke="#888" stroke-width="1.2"/></svg></span>
    </div>
  </nav>

  <div class="col col-a">
    <article class="card">
      <div class="card-media" style="height:231px;background:linear-gradient(180deg,#4a4a4a 0%,#1e1e1e 60%,#3a3d40 100%)" role="img" aria-label="Black cylindrical smart speaker standing on a desk">
        <div class="tags"><span class="tag tag-home">HOME</span><span class="tag tag-speakers">SPEAKERS</span></div>
      </div>
      <h3 class="card-title">The Nimbus Orb...One Of Our Essentials</h3>
      <div class="meta"><span class="author"><i class="avatar"></i>Rowan Ellis</span><span class="date">Aug 11, 2016</span></div>
    </article>
    <article class="card">
      <div class="card-media" style="height:333px;background:linear-gradient(180deg,#3c4146 0%,#262626 50%,#7a6048 100%)" role="img" aria-label="Video camera with a fluffy microphone on a wooden desk">
        <div class="tags"><span class="tag tag-home">HOME</span></div>
      </div>
      <h3 class="card-title">The Nimbus Orb...One Of Our Essentials</h3>
      <div class="meta"><span class="author"><i class="avatar"></i>Rowan Ellis</span><span class="date">Aug 11, 2016</span></div>
    </article>
    <article class="card">
      <div class="card-media" style="height:232px;background:linear-gradient(135deg,#6e6a62 0%,#a8a29a 40%,#4fb7b2 70%,#ddd8d2 100%)" role="img" aria-label="Teal portable speaker on a table in a café">
        <div class="tags"><span class="tag tag-speakers">SPEAKERS</span></div>
      </div>
      <h3 class="card-title">The Nimbus Orb...One Of Our Essentials</h3>
      <div class="meta"><span class="author"><i class="avatar"></i>Rowan Ellis</span><span class="date">Aug 11, 2016</span></div>
    </article>
    <article class="card">
      <div class="card-media" style="height:181px;background:linear-gradient(180deg,#3a3c3e 0%,#1f1f1f 60%,#34373a 100%)" role="img" aria-label="Black cylindrical smart speaker standing on a desk">
        <div class="tags"><span class="tag tag-home">HOME</span><span class="tag tag-speakers">SPEAKERS</span></div>
      </div>
      <h3 class="card-title">The Nimbus Orb...One Of Our Essentials</h3>
      <div class="meta"><span class="author"><i class="avatar"></i>Rowan Ellis</span><span class="date">Aug 11, 2016</span></div>
    </article>
  </div>

  <div class="col col-b">
    <article class="card">
      <div class="card-media" style="height:335px;background:linear-gradient(135deg,#6e6a62 0%,#a8a29a 40%,#4fb7b2 70%,#ddd8d2 100%)" role="img" aria-label="Teal portable speaker on a table in a café">
        <div class="tags"><span class="tag tag-home">HOME</span></div>
      </div>
      <h3 class="card-title">The Nimbus Orb...One Of Our Essentials</h3>
      <div class="meta"><span class="author"><i class="avatar"></i>Rowan Ellis</span><span class="date">Aug 11, 2016</span></div>
    </article>
    <article class="card">
      <div class="card-media" style="height:435px;background:linear-gradient(180deg,#e8eaea 0%,#d4d2cc 55%,#c9c7c2 100%)" role="img" aria-label="Bright modern white kitchen with bar stools at an island">
        <div class="tags"><span class="tag tag-home">HOME</span><span class="tag tag-speakers">SPEAKERS</span></div>
      </div>
      <h3 class="card-title">The Nimbus Orb...One Of Our Essentials</h3>
      <div class="meta"><span class="author"><i class="avatar"></i>Rowan Ellis</span><span class="date">Aug 11, 2016</span></div>
    </article>
    <article class="card">
      <div class="card-media" style="height:333px;background:linear-gradient(180deg,#3c4146 0%,#262626 50%,#7a6048 100%)" role="img" aria-label="Video camera with a fluffy microphone on a wooden desk">
        <div class="tags"><span class="tag tag-speakers">SPEAKERS</span></div>
      </div>
      <h3 class="card-title">The Nimbus Orb...One Of Our Essentials</h3>
      <div class="meta"><span class="author"><i class="avatar"></i>Rowan Ellis</span><span class="date">Aug 11, 2016</span></div>
    </article>
  </div>

  <div class="load-more">LOAD MORE</div>

  <footer class="footer">Copyright © 2016 <b>PIVLOGUIDE</b> |&nbsp; All Rights Reserved.</footer>
</div>
</body>
</html>
```